Need a business card for auto body business

Needs to be on card:
Ridge Crest Collision Marco Bellanti / Licensed Appraiser PGRC Corp Facebook Logo
418 Orchard Avenue
Alderbrook Eastvale 02597
T 555-555-0193
F 555-555-0147
pinegroveridgecrest.com
info@pinegroveridgecrest.com
https://www.friendlink.example/Ridge.Crest.Collision

I will attach a sample of the old Business card

Target Market(s)

Professional, business, classy,

Industry/Entity Type

Business

```html
<!DOCTYPE html>
<html lang="en">
<head>
<meta charset="utf-8">
<title>Ridge Crest Collision – Business Card</title>
<link rel="stylesheet" href="https://fonts.googleapis.com/css2?family=Arimo:wght@400;700&family=Kaushan+Script&display=swap">
<style>
  :root {
    --page-bg: #ffffff;
    --page-frame: #9a9a9a;
    --card-dark: #1b1b1d;
    --card-mid: #2e2e31;
    --streak: rgba(255,255,255,0.14);
    --brand-red: #d8261b;
    --text-light: #f4f4f4;
    --text-soft: #d8d8d8;
    --icon-blue: #3b5998;
  }
  * { margin: 0; padding: 0; box-sizing: border-box; }
  html, body { width: 1200px; height: 664px; overflow: hidden; background: var(--page-bg); }
  .canvas {
    position: relative; width: 1200px; height: 664px;
    border: 1px solid var(--page-frame);
    font-family: "Arimo", Arial, sans-serif;
  }
  .card {
    position: absolute; width: 519px; height: 305px;
    background:
      linear-gradient(155deg, transparent 0 8%, var(--streak) 12%, transparent 16%, var(--streak) 20%, transparent 25%, var(--streak) 29%, transparent 36%),
      linear-gradient(135deg, var(--card-mid) 0%, var(--card-dark) 45%, var(--card-dark) 100%);
    color: var(--text-light);
    overflow: hidden;
  }
  .card--front { left: 104px; top: 80px; }
  .card--back { left: 544px; top: 273px; }

  .brand-name {
    position: absolute; left: 0; right: 0; text-align: center; white-space: nowrap;
    font-family: "Arimo", Arial, sans-serif; font-weight: 700;
    text-transform: uppercase; color: var(--brand-red);
    letter-spacing: 1px; line-height: 1;
  }
  .card--front .brand-name { top: 126px; font-size: 27px; }
  .card--back .brand-name { top: 118px; font-size: 17px; }

  .tagline {
    position: absolute; left: 0; right: 0; text-align: center; white-space: nowrap;
    font-family: "Kaushan Script", cursive; color: var(--text-light); line-height: 1;
  }
  .card--front .tagline { top: 208px; font-size: 28px; }
  .card--back .tagline { top: 184px; font-size: 19px; }

  .person { position: absolute; right: 24px; top: 24px; text-align: right; line-height: 1; }
  .person-name { font-size: 19px; color: var(--text-light); }
  .person-title { font-size: 12.5px; color: var(--text-soft); margin-top: 6px; }

  .contact {
    position: absolute; left: 0; right: 0; top: 216px;
    text-align: center; font-size: 12.5px; line-height: 17.5px; color: var(--text-soft);
    white-space: nowrap;
  }
  .social-square {
    display: inline-block; width: 11px; height: 11px; background: var(--icon-blue);
    vertical-align: -1px; margin-right: 6px;
  }
</style>
</head>
<body>
<div class="canvas">
  <section class="card card--front">
    <div class="brand-name">Ridge Crest Collision</div>
    <div class="tagline">Expert Auto Body Repair</div>
  </section>

  <section class="card card--back">
    <div class="person">
      <div class="person-name">Marco Bellanti</div>
      <div class="person-title">Licensed Appraiser PGRC Corp</div>
    </div>
    <div class="brand-name">Ridge Crest Collision</div>
    <div class="tagline">Expert Auto Body Repair</div>
    <div class="contact">
      <div>418 Orchard Avenue, Alderbrook Eastvale 02597</div>
      <div>T 555-555-0193, F 555-555-0147</div>
      <div>E pinegroveridgecrest.com, info@pinegroveridgecrest.com</div>
      <div><span class="social-square"></span>https://www.friendlink.example/Ridge.Crest.Collision</div>
    </div>
  </section>
</div>
</body>
</html>
```